Power Point Digital Signage Template Needed

The North Calloway Health Centre and Pharmacy (ourcalloway.example) needs a power point digital signage template that is customizable and pulls pertinent local information like weather, news and generic health tips. Please use design and colors from art work and website. We would need the power point project to be able to be read clearly at a distance of around 10 - 15 feet and provide the viewer with all information about our clinic/pharmacy services while attracting their attention with local news or weather reports and health tips.

Target Market(s)

People in waiting room, healthcare , family doctor patients to drive pharmacy business and healthcare centre awareness

Industry/Entity Type

Healthcare

Font styles to use
Serif
Sans Serif

Colors

Designer to choose colors to be used in the design.

Requirements
Must have
• Links to real time local weather
• Scrolling News
• Scrolling Health tips
• Fully Customizable
• Power Point Format
• Multiple Slides for each feature (example 1 for real time weather, 1 slide for news, 1 slide for cliinic hours etc)
• At least 20 customizable slides on contiual rotation

```html
<!DOCTYPE html>
<html lang="en">
<head>
<meta charset="utf-8">
<title>North Calloway Health Centre and Pharmacy – Weather Forecast</title>
<link rel="stylesheet" href="https://fonts.googleapis.com/css2?family=Montserrat:wght@600;700&family=Roboto+Condensed:wght@400;700&display=swap">
<style>
  :root {
    --brand-green: #1f8a3a;
    --band-dark: #383838;
    --white: #ffffff;
    --ink: #222222;
    --muted: #8a8a8a;
    --rule: #e2e2e2;
    --weather-blue: #1482c4;
    --sky-top: #4f86d2;
    --sky-bottom: #8fb6e6;
    --navy: #1d3557;
    --sun: #f6b81a;
    --warm-yellow: #f2b21c;
    --warm-orange: #ee7a33;
    --warm-red: #e2553a;
    --scroll: #c4c4c4;
    --field: #ececec;
  }
  * { box-sizing: border-box; margin: 0; padding: 0; }
  html, body { width: 1200px; height: 678px; overflow: hidden; background: var(--white); }
  .slide { position: relative; width: 1200px; height: 678px; overflow: hidden; font-family: "Roboto Condensed", sans-serif; color: var(--ink); }

  .scene-backdrop {
    position: absolute; inset: 0;
    background: linear-gradient(180deg, #dce8f1 0%, #eef3f6 35%, #f3f6f3 55%, #bcd39a 66%, #86b253 78%, #5e8f38 100%);
  }

  .brand { position: absolute; left: 64px; top: 165px; width: 234px; text-align: center; color: var(--brand-green); font-family: "Montserrat", sans-serif; font-weight: 700; }
  .brand-mark { width: 66px; height: 66px; border-radius: 50%; background: var(--brand-green); margin: 0 auto 12px; }
  .brand-name { font-size: 27px; line-height: 1.05; letter-spacing: 0.5px; }
  .brand-sub { font-size: 10.5px; letter-spacing: 1.6px; margin-top: 6px; }

  .title-band { position: absolute; left: 376px; top: 71px; width: 76px; height: 336px; background: var(--band-dark); }
  .title-band h1 { position: absolute; left: 50%; top: 50%; transform: translate(-50%, -50%) rotate(-90deg); white-space: nowrap; color: var(--white); font-family: "Montserrat", sans-serif; font-weight: 700; font-size: 33px; letter-spacing: 0.5px; }

  .weather-widget { position: absolute; left: 452px; top: 71px; width: 685px; height: 430px; background: var(--white); overflow: hidden; }

  .site-nav { position: absolute; left: 0; top: 0; width: 648px; height: 26px; display: flex; align-items: center; font-size: 9px; font-weight: 700; white-space: nowrap; }
  .site-nav > * { flex-shrink: 0; }
  .site-name { width: 90px; padding-left: 31px; font-size: 14px; letter-spacing: 1px; font-weight: 700; }
  .sign-in { width: 108px; display: flex; align-items: center; gap: 4px; padding-left: 10px; border-left: 1px solid var(--rule); height: 100%; }
  .sign-in i { width: 10px; height: 10px; border-radius: 50%; background: var(--ink); display: block; }
  .nav-item { padding: 0 7px; height: 100%; display: flex; align-items: center; border-left: 1px solid var(--rule); }
  .nav-more { width: 72px; justify-content: space-between; }
  .nav-search { margin-left: auto; width: 126px; height: 16px; background: var(--field); display: flex; align-items: center; justify-content: space-between; padding: 0 4px; font-weight: 700; }

  .weather-header { position: absolute; left: 0; top: 26px; width: 648px; height: 40px; background: var(--weather-blue); }
  .weather-header h2 { position: absolute; left: 31px; top: 3px; color: var(--white); font-family: "Roboto Condensed", sans-serif; font-weight: 400; font-size: 30px; line-height: 34px; letter-spacing: 0.5px; }
  .city-search { position: absolute; left: 168px; top: 6px; width: 476px; height: 27px; background: var(--white); display: flex; align-items: center; justify-content: space-between; padding: 0 6px; font-size: 11px; color: #555; }

  .location-sky { position: absolute; left: 0; top: 66px; width: 648px; height: 131px; background: linear-gradient(180deg, var(--sky-top), var(--sky-bottom)); }
  .location-name { position: absolute; left: 31px; top: 73px; color: var(--white); font-size: 15px; line-height: 20px; }
  .add-location { position: absolute; left: 93px; top: 71px; width: 130px; height: 20px; background: var(--navy); color: var(--white); font-size: 9px; display: flex; align-items: center; gap: 5px; padding-left: 6px; white-space: nowrap; }
  .add-location b { font-size: 13px; }

  .today-card { position: absolute; left: 31px; top: 100px; width: 255px; height: 97px; background: var(--white); border-top: 5px solid var(--sun); }
  .today-card h3 { position: absolute; left: 10px; top: 12px; font-weight: 400; font-size: 15px; }
  .today-card .icon { position: absolute; left: 12px; top: 36px; width: 44px; height: 44px; }
  .today-temps { position: absolute; left: 72px; top: 40px; font-size: 14px; line-height: 19px; text-align: right; }
  .today-divider { position: absolute; left: 105px; top: 40px; width: 1px; height: 48px; background: #555; }
  .today-summary { position: absolute; left: 116px; top: 40px; font-size: 12px; white-space: nowrap; }

  .day-strip { position: absolute; left: 286px; top: 138px; display: flex; }
  .day { width: 68px; height: 59px; background: var(--white); border-left: 1px solid var(--rule); border-bottom: 5px solid var(--warm-orange); position: relative; font-size: 8.5px; color: #444; white-space: nowrap; }
  .day span { position: absolute; left: 5px; top: 5px; }
  .day .icon { position: absolute; left: 5px; top: 20px; width: 26px; height: 26px; }
  .day .temps { position: absolute; right: 6px; top: 22px; text-align: right; line-height: 13px; font-size: 10px; }
  .day .temps small { font-size: 8px; }
  .day.yellow { border-bottom-color: var(--warm-yellow); }
  .day.red { border-bottom-color: var(--warm-red); }
  .day.partial { width: 20px; overflow: hidden; }
  .strip-next { position: absolute; left: 643px; top: 138px; width: 22px; height: 59px; background: var(--weather-blue); color: var(--white); font-size: 14px; font-weight: 700; display: flex; align-items: center; justify-content: center; }
  .strip-prev { position: absolute; left: 12px; top: 138px; width: 19px; height: 59px; background: #b8cbe6; color: var(--white); display: flex; align-items: center; justify-content: center; font-size: 12px; }

  .h-scroll { position: absolute; left: 40px; top: 199px; width: 600px; height: 8px; background: #f1f1f1; }
  .h-scroll i { position: absolute; left: 8px; top: 1px; width: 320px; height: 6px; background: var(--scroll); }
  .v-scroll { position: absolute; right: 0; top: 0; width: 9px; height: 430px; background: #f1f1f1; }
  .v-scroll i { position: absolute; left: 1px; top: 10px; width: 7px; height: 100px; background: var(--scroll); }

  .hourly { position: absolute; left: 31px; top: 208px; display: flex; height: 206px; }
  .hour { position: relative; width: 41px; height: 100%; border-right: 1px solid var(--rule); font-size: 8.5px; font-weight: 700; text-align: center; }
  .hour .time { position: absolute; left: 0; right: 0; top: 8px; }
  .hour .icon { position: absolute; left: 11px; top: calc(var(--y) - 10px); width: 20px; height: 20px; }
  .hour .temp { position: absolute; left: 0; right: 0; top: calc(var(--y) + 12px); font-size: 9.5px; font-weight: 400; }
  .hour .rain { position: absolute; left: 0; right: 0; top: 148px; color: var(--muted); font-size: 9px; letter-spacing: 1px; }
  .hour .rain-pct { position: absolute; left: 0; right: 0; top: 162px; color: var(--muted); font-size: 7px; font-weight: 400; }
  .hour .wind { position: absolute; left: 13px; top: 181px; width: 15px; height: 15px; border: 1px solid var(--ink); border-radius: 50%; font-size: 7px; font-weight: 400; line-height: 13px; }
  .hourly-prev { position: absolute; left: 12px; top: 286px; width: 19px; height: 59px; background: #f0f0f0; color: #aaa; display: flex; align-items: center; justify-content: center; font-size: 12px; }
  .hourly-next { position: absolute; left: 441px; top: 286px; width: 21px; height: 59px; background: var(--weather-blue); color: var(--white); display: flex; align-items: center; justify-content: center; font-size: 13px; font-weight: 700; }
  .hourly-scroll { position: absolute; left: 31px; top: 415px; width: 410px; height: 8px; background: #f1f1f1; }
  .hourly-scroll i { position: absolute; left: 10px; top: 1px; width: 148px; height: 6px; background: var(--scroll); }
</style>
</head>
<body>
<svg width="0" height="0" style="position:absolute" aria-hidden="true">
  <defs>
    <symbol id="icon-sun" viewBox="-12 -12 24 24">
      <g stroke="#f6b81a" stroke-width="1.6" stroke-linecap="round">
        <line x1="0" y1="-11" x2="0" y2="-8"/><line x1="0" y1="8" x2="0" y2="11"/>
        <line x1="-11" y1="0" x2="-8" y2="0"/><line x1="8" y1="0" x2="11" y2="0"/>
        <line x1="-7.8" y1="-7.8" x2="-5.7" y2="-5.7"/><line x1="5.7" y1="5.7" x2="7.8" y2="7.8"/>
        <line x1="-7.8" y1="7.8" x2="-5.7" y2="5.7"/><line x1="5.7" y1="-5.7" x2="7.8" y2="-7.8"/>
      </g>
      <circle r="6" fill="#ffc928" stroke="#f6b81a" stroke-width="1"/>
    </symbol>
    <symbol id="icon-cloud-sun" viewBox="-12 -12 24 24">
      <use href="#icon-sun" x="-8" y="-8" width="20" height="20"/>
      <path d="M-10 6 a4 4 0 0 1 3 -6 a5 5 0 0 1 9 -1 a3.5 3.5 0 0 1 3 7 z" fill="#fff" stroke="#777" stroke-width="1.2"/>
    </symbol>
  </defs>
</svg>

<main class="slide">
  <div class="scene-backdrop" role="img" aria-label="Photograph of a bright sky over green rolling hills with four adults jogging across the grass"></div>

  <div class="brand">
    <div class="brand-mark"></div>
    <div class="brand-name">North Calloway</div>
    <div class="brand-sub">HEALTH CENTRE AND PHARMACY</div>
  </div>

  <div class="title-band"><h1>Weather Forecast</h1></div>

  <section class="weather-widget">
    <nav class="site-nav">
      <span class="site-name">SKYLINE</span>
      <span class="sign-in"><i></i>Sign in</span>
      <span class="nav-item">News</span>
      <span class="nav-item">Sport</span>
      <span class="nav-item">Weather</span>
      <span class="nav-item">Shop</span>
      <span class="nav-item">Earth</span>
      <span class="nav-item">Travel</span>
      <span class="nav-item nav-more">More <span>▾</span></span>
      <span class="nav-search">Search <span>⌕</span></span>
    </nav>

    <header class="weather-header">
      <h2>WEATHER</h2>
      <div class="city-search"><span>Enter a city</span><span style="font-size:17px">⌕</span></div>
    </header>

    <div class="location-sky"></div>
    <div class="location-name">Winnipeg</div>
    <div class="add-location"><b>+</b> Add to My Locations</div>

    <div class="strip-prev">‹</div>
    <article class="today-card">
      <h3>Today</h3>
      <svg class="icon"><use href="#icon-sun"/></svg>
      <div class="today-temps">13°<br>1°</div>
      <div class="today-divider"></div>
      <div class="today-summary">Sunny and breezy</div>
    </article>

    <div class="day-strip">
      <div class="day yellow"><span>Tomorrow</span><svg class="icon"><use href="#icon-cloud-sun"/></svg><div class="temps">16°<br><small>5°</small></div></div>
      <div class="day red"><span>Sat 12th</span><svg class="icon"><use href="#icon-sun"/></svg><div class="temps">23°<br><small>10°</small></div></div>
      <div class="day red"><span>Sun 13th</span><svg class="icon"><use href="#icon-sun"/></svg><div class="temps">28°<br><small>10°</small></div></div>
      <div class="day red"><span>Mon 14th</span><svg class="icon"><use href="#icon-sun"/></svg><div class="temps">25°<br><small>9°</small></div></div>
      <div class="day"><span>Tue 15th</span><svg class="icon"><use href="#icon-sun"/></svg><div class="temps">23°<br><small>8°</small></div></div>
      <div class="day yellow partial"><span>Wed</span></div>
    </div>
    <div class="strip-next">›</div>

    <div class="h-scroll"><i></i></div>

    <div class="hourly-prev">‹</div>
    <div class="hourly">
      <div class="hour" style="--y:111px"><span class="time">0800</span><svg class="icon"><use href="#icon-sun"/></svg><span class="temp">3°</span><span class="rain">∴</span><span class="rain-pct">0%</span><span class="wind">5</span></div>
      <div class="hour" style="--y:103px"><span class="time">0900</span><svg class="icon"><use href="#icon-sun"/></svg><span class="temp">4°</span><span class="rain">∴</span><span class="rain-pct">0%</span><span class="wind">6</span></div>
      <div class="hour" style="--y:95px"><span class="time">1000</span><svg class="icon"><use href="#icon-sun"/></svg><span class="temp">5°</span><span class="rain">∴</span><span class="rain-pct">0%</span><span class="wind">7</span></div>
      <div class="hour" style="--y:80px"><span class="time">1100</span><svg class="icon"><use href="#icon-sun"/></svg><span class="temp">7°</span><span class="rain">∴</span><span class="rain-pct">1%</span><span class="wind">7</span></div>
      <div class="hour" style="--y:65px"><span class="time">1200</span><svg class="icon"><use href="#icon-sun"/></svg><span class="temp">9°</span><span class="rain">∴</span><span class="rain-pct">1%</span><span class="wind">7</span></div>
      <div class="hour" style="--y:57px"><span class="time">1300</span><svg class="icon"><use href="#icon-sun"/></svg><span class="temp">10°</span><span class="rain">∴</span><span class="rain-pct">1%</span><span class="wind">6</span></div>
      <div class="hour" style="--y:49px"><span class="time">1400</span><svg class="icon"><use href="#icon-sun"/></svg><span class="temp">11°</span><span class="rain">∴</span><span class="rain-pct">1%</span><span class="wind">6</span></div>
      <div class="hour" style="--y:41px"><span class="time">1500</span><svg class="icon"><use href="#icon-sun"/></svg><span class="temp">12°</span><span class="rain">∴</span><span class="rain-pct">0%</span><span class="wind">6</span></div>
      <div class="hour" style="--y:41px"><span class="time">1600</span><svg class="icon"><use href="#icon-sun"/></svg><span class="temp">12°</span><span class="rain">∴</span><span class="rain-pct">0%</span><span class="wind">6</span></div>
      <div class="hour" style="--y:41px"><span class="time">1700</span><svg class="icon"><use href="#icon-sun"/></svg><span class="temp">12°</span><span class="rain">∴</span><span class="rain-pct">0%</span><span class="wind">6</span></div>
    </div>
    <div class="hourly-next">›</div>
    <div class="hourly-scroll"><i></i></div>

    <div class="v-scroll"><i></i></div>
  </section>
</main>
</body>
</html>
```